Business cards

Dog breeder selling very high end expensive pets so design must be modern, simple (with the focus being on the photos) and upscale. Would like a full photo on each side of the card with text as an accent more then as the focus.
I would like the name of the business to be large and bold (possibly modern cursive font) and centered preferably but am open to other options
Need the French bulldogs on the front if the card if not both. I was thinking of one full photo on each side but as long as the French Bulldogs are the focus I'm open to all options. The French bulldogs are the ones in the photo with three puppies pictured
Info needed on the card:
Velvet Kennels
www.velvetkennels.com
thevelvetkennel@quillmail.net
(555) 214-7389
On the back:
Quality pets and champion show dogs

```html
<!DOCTYPE html>
<html lang="en">
<head>
<meta charset="utf-8">
<title>Velvet Kennels – Business Card</title>
<link rel="stylesheet" href="https://fonts.googleapis.com/css2?family=Cinzel:wght@500&family=Marcellus&display=swap">
<style>
  :root {
    --backdrop: #4fc4e3;
    --card-yellow: #ffcb05;
    --band-charcoal: #333333;
    --ink: #111111;
    --frame-black: #0a0a0a;
    --photo-light: #f4f1ee;
    --photo-warm: #b9865c;
    --pups-tone-a: #8f8a82;
    --pups-tone-b: #3a3735;
  }
  html, body {
    margin: 0;
    width: 1200px;
    height: 1000px;
    overflow: hidden;
    background: var(--backdrop);
  }
  .business-card {
    position: absolute;
    left: 150px;
    top: 240px;
    width: 900px;
    height: 520px;
    background: var(--card-yellow);
    overflow: hidden;
    box-shadow: 0 18px 40px rgba(0,0,0,0.18);
  }
  .card-shapes {
    position: absolute;
    inset: 0;
  }
  .business-name {
    position: absolute;
    left: 45px;
    top: 36px;
    margin: 0;
    font-family: "Cinzel", serif;
    font-weight: 500;
    font-size: 48px;
    line-height: 1.1;
    color: var(--ink);
    letter-spacing: 0.5px;
    white-space: nowrap;
  }
  .contact-list {
    position: absolute;
    left: 60px;
    top: 120px;
    margin: 0;
    padding: 0;
    list-style: none;
    font-family: "Marcellus", serif;
    font-size: 34px;
    line-height: 38px;
    color: var(--ink);
    white-space: nowrap;
  }
  .photo-frame {
    position: absolute;
    left: 55px;
    top: 268px;
    width: 340px;
    height: 190px;
    background: var(--frame-black);
    border-radius: 30px 6px 40px 6px;
    padding: 12px;
    box-sizing: border-box;
  }
  .puppy-photo {
    width: 100%;
    height: 100%;
    border-radius: 22px 2px 30px 2px;
    background: radial-gradient(ellipse at 50% 60%, var(--photo-warm) 0%, #d9c2ab 35%, var(--photo-light) 70%);
  }
  .frenchie-photo {
    position: absolute;
    left: 565px;
    top: 318px;
    width: 300px;
    height: 190px;
    border-radius: 40px 40px 10px 10px;
    background: linear-gradient(90deg, var(--pups-tone-a) 0%, var(--pups-tone-b) 50%, #a49b8e 100%);
  }
</style>
</head>
<body>
  <article class="business-card">
    <svg class="card-shapes" width="900" height="520" viewBox="0 0 900 520" aria-hidden="true">
      <path class="top-band" fill="var(--band-charcoal)" d="M430 0 H900 V150 L565 92 C515 84 480 30 430 0 Z"/>
      <path class="bottom-band" fill="var(--band-charcoal)" d="M0 450 H490 C530 455 550 495 585 520 H0 Z"/>
    </svg>

    <h1 class="business-name">Velvet Kennels</h1>
    <ul class="contact-list">
      <li class="contact-web">www.velvetkennels.com</li>
      <li class="contact-email">thevelvetkennel@quillmail.net</li>
      <li class="contact-phone">(555) 214-7389</li>
    </ul>

    <div class="photo-frame">
      <div class="puppy-photo" role="img" aria-label="Bulldog puppy lying beside a full food bowl"></div>
    </div>

    <div class="frenchie-photo" role="img" aria-label="Three French bulldog puppies sitting side by side"></div>
  </article>
</body>
</html>
```